CREATIVE DESIGNERS NEEDED & Enhance Your Business Card Portfolio

Artistic, unique, professional real estate card needed - see attached documents "B-cards.pdf" for all details and examples.True Designers will see other projects of ours come online here. We like long-term relationships for creative designers. This business card will be used in two U.S. states and is central to our business and other future marketing.

Target Market(s)

Buyers and Sellers of real estate

Industry/Entity Type

Real Estate Agent

Contact Information for Business Card

See attached detailed brief

Font styles to use
Other font styles liked:
• ADAM.CG PRO & NewsGoth BT

Requirements
Must have
• 2-sided, creative (non-traditional layout/design). Incorporate a cut-out (for texture, and make it fun! No boring templates for this card -
Nice to have
• See attached detailed brief
Should not have

```html
<!DOCTYPE html>
<html lang="en">
<head>
<meta charset="utf-8">
<title>Carver Group Real Estate – Business Card</title>
<link rel="stylesheet" href="https://fonts.googleapis.com/css2?family=Lato:wght@300;400;700&display=swap">
<style>
  :root {
    --backdrop: #3b3431;
    --card: #0d0d0d;
    --card-edge: #1c1c1c;
    --silver: #d9d9d9;
    --silver-soft: #b5b5b5;
    --photo-light: #8a8a8a;
    --photo-dark: #1e1e1e;
  }
  * { margin: 0; padding: 0; box-sizing: border-box; }
  html, body {
    width: 1200px; height: 900px; overflow: hidden;
    background: var(--backdrop);
    font-family: "Lato", sans-serif;
  }
  .stage { position: relative; width: 1200px; height: 900px; }
  .card {
    position: absolute; top: 296px;
    width: 540px; height: 309px;
    background: var(--card);
    border: 1px solid var(--card-edge);
    border-radius: 4px;
    overflow: hidden;
    color: var(--silver);
  }
  .card--front { left: 45px; }
  .card--back { left: 615px; }

  .portrait {
    position: absolute; left: 0; bottom: 0;
    width: 260px; height: 240px;
    background: radial-gradient(ellipse at 50% 40%, var(--photo-light) 0%, #4a4a4a 45%, var(--photo-dark) 80%);
  }

  .brand {
    display: flex; align-items: center; gap: 10px;
  }
  .brand__mark {
    width: 34px; height: 34px;
    border: 2px solid var(--silver);
  }
  .brand__name {
    font-weight: 700; letter-spacing: 1.5px;
    line-height: 1.05; text-transform: uppercase;
    color: var(--silver);
  }

  .card--front .brand { position: absolute; left: 290px; top: 42px; }
  .card--front .brand__name { font-size: 19px; }

  .region {
    position: absolute; left: 290px; top: 104px;
    font-size: 14px; color: var(--silver);
  }
  .agent { position: absolute; left: 300px; top: 150px; }
  .agent__name { font-size: 19px; font-weight: 400; letter-spacing: 0.5px; text-transform: uppercase; }
  .agent__title { font-size: 14px; color: var(--silver-soft); margin-top: 2px; }
  .contact { list-style: none; margin-top: 18px; }
  .contact__item {
    display: flex; align-items: center; gap: 6px;
    font-size: 17px; line-height: 1.3;
  }
  .contact__icon { width: 12px; height: 14px; fill: var(--silver); }

  .card--back .brand { position: absolute; left: 50%; top: 70px; transform: translateX(-50%); }
  .card--back .brand__mark { width: 44px; height: 44px; }
  .card--back .brand__name { font-size: 24px; }

  .partner {
    position: absolute; left: 50%; top: 158px; transform: translateX(-50%);
    display: flex; align-items: center; gap: 8px;
  }
  .partner__badge { width: 22px; height: 22px; background: #8c8c8c; transform: rotate(45deg); }
  .partner__name { font-size: 15px; letter-spacing: 1px; text-transform: uppercase; color: var(--silver); }

  .services {
    position: absolute; left: 0; right: 0; top: 222px;
    text-align: center;
    font-size: 13px; font-weight: 300; letter-spacing: 1.5px;
    color: var(--silver-soft); text-transform: uppercase;
  }
</style>
</head>
<body>
<main class="stage">
  <section class="card card--front">
    <div class="portrait" role="img" aria-label="Black and white portrait photo of the agent"></div>
    <div class="brand">
      <span class="brand__mark"></span>
      <span class="brand__name">Carver Group<br>Real Estate</span>
    </div>
    <p class="region">San Diego &amp; Phoenix</p>
    <div class="agent">
      <h1 class="agent__name">Dean Carver</h1>
      <p class="agent__title">Broker Associate Realtor</p>
      <ul class="contact">
        <li class="contact__item">
          <svg class="contact__icon" viewBox="0 0 12 14"><path d="M1 3c0-1 1-2 2-2l1 3-1.2 1c.6 1.8 1.8 3.2 3.4 4.1L7.5 8l3 1.3c0 1.2-1 2.2-2 2.2C4.5 11.5 1 7.5 1 3z"/></svg>
          (800) Sold-Now
        </li>
        <li class="contact__item">
          <svg class="contact__icon" viewBox="0 0 12 14"><path d="M3 0h6a1 1 0 0 1 1 1v12a1 1 0 0 1-1 1H3a1 1 0 0 1-1-1V1a1 1 0 0 1 1-1zm0 2v9h6V2zm3 10a.7.7 0 1 0 0 1.4A.7.7 0 0 0 6 12z"/></svg>
          (555) 014-2837
        </li>
      </ul>
    </div>
  </section>

  <section class="card card--back">
    <div class="brand">
      <span class="brand__mark"></span>
      <span class="brand__name">Carver Group<br>Real Estate</span>
    </div>
    <div class="partner">
      <span class="partner__badge"></span>
      <span class="partner__name">Keystone Realty</span>
    </div>
    <p class="services">Resedential | Investment | Development</p>
  </section>
</main>
</body>
</html>
```